Business Card Design

I will be finding aged care homes for those who need placement.
Assisting with all of the paperwork.
I would like Australian wattle picture on the card/ logo please
Industry/Entity Type
Business
Contact Information for Business Card
Elder Path Solutions
Moira Delacombe
PH: 0438 592 163
Email: elderpathsolutions@mailbox.example
ABN: 31904628375
PO Box 3198, Kellmore QLD 4587

```html
<!DOCTYPE html>
<html lang="en">
<head>
<meta charset="utf-8">
<title>Elder Path Solutions — Business Card</title>
<link rel="stylesheet" href="https://fonts.googleapis.com/css2?family=Cinzel:wght@400;600&family=Lato:wght@400&display=swap">
<style>
  :root {
    --page-bg: #1c1c1c;
    --card-bg: #2c2c2c;
    --gold: #c9a43a;
    --gold-soft: #bfa04a;
    --wattle-yellow: #d9c33a;
    --leaf-green: #7f8a6a;
  }
  html, body {
    margin: 0;
    width: 1200px;
    height: 1000px;
    overflow: hidden;
    background: var(--page-bg);
  }
  .canvas {
    position: relative;
    width: 1200px;
    height: 1000px;
  }
  .business-card {
    position: absolute;
    left: 100px;
    top: 214px;
    width: 1000px;
    height: 572px;
    background: var(--card-bg);
    box-shadow: 0 20px 50px rgba(0,0,0,0.6);
    overflow: hidden;
  }
  .wattle-artwork {
    position: absolute;
    left: 0;
    top: 70px;
    width: 400px;
    height: 502px;
    background:
      radial-gradient(ellipse at 55% 45%, rgba(217,195,58,0.75) 0%, rgba(217,195,58,0.35) 40%, rgba(127,138,106,0.35) 65%, rgba(44,44,44,0) 85%);
  }
  .card-details {
    position: absolute;
    right: 70px;
    top: 70px;
    width: 560px;
    text-align: right;
    color: var(--gold);
  }
  .business-name {
    margin: 0;
    font-family: "Cinzel", serif;
    font-weight: 600;
    font-size: 56px;
    line-height: 1.0;
    letter-spacing: 1px;
  }
  .abn {
    margin: 8px 0 0;
    font-family: "Lato", sans-serif;
    font-size: 17px;
    color: var(--gold-soft);
  }
  .person-name {
    margin: 64px 0 0;
    font-family: "Cinzel", serif;
    font-weight: 400;
    font-size: 40px;
    letter-spacing: 1px;
    color: var(--gold-soft);
  }
  .contact-list {
    list-style: none;
    margin: 48px 0 0;
    padding: 0;
    font-family: "Lato", sans-serif;
    font-size: 23px;
    color: var(--gold-soft);
  }
  .contact-list li {
    margin-bottom: 16px;
    display: flex;
    justify-content: flex-end;
    align-items: center;
    gap: 12px;
  }
  .contact-icon {
    width: 22px;
    height: 22px;
    flex: none;
  }
</style>
</head>
<body>
<main class="canvas">
  <section class="business-card">
    <div class="wattle-artwork" role="img" aria-label="Botanical illustration of an Australian wattle branch with yellow flower puffs and grey-green leaves"></div>

    <div class="card-details">
      <h1 class="business-name">Elder Path<br>Solutions</h1>
      <p class="abn">ABN: 31904628375</p>
      <h2 class="person-name">Moira Delacombe</h2>
      <ul class="contact-list">
        <li>
          <span>0438 592 163</span>
          <svg class="contact-icon" viewBox="0 0 24 24" aria-hidden="true">
            <path fill="var(--gold)" d="M6.6 10.8a15.1 15.1 0 0 0 6.6 6.6l2.2-2.2a1 1 0 0 1 1-.25 11.4 11.4 0 0 0 3.6.57 1 1 0 0 1 1 1V20a1 1 0 0 1-1 1A17 17 0 0 1 3 4a1 1 0 0 1 1-1h3.5a1 1 0 0 1 1 1c0 1.25.2 2.45.57 3.57a1 1 0 0 1-.25 1z"/>
          </svg>
        </li>
        <li>
          <span>elderpathsolutions@mailbox.example</span>
          <svg class="contact-icon" viewBox="0 0 24 24" aria-hidden="true">
            <rect x="2" y="5" width="20" height="14" fill="var(--gold)"/>
            <path d="M2 5l10 8 10-8" fill="none" stroke="var(--card-bg)" stroke-width="1.6"/>
          </svg>
        </li>
        <li>
          <span>PO Box 3198, Kellmore QLD 4587</span>
          <span class="contact-icon" aria-hidden="true"></span>
        </li>
      </ul>
    </div>
  </section>
</main>
</body>
</html>
```